Veltracore Needs a Poster to Advertise a New Membership Offer

We need a Poster design for Veltracore Fitness Studio.
A first of it's kind membership, The Veltracore Fitness Studio combines the skills of our industry-leading Physiotherapists, Strength Coaches and Massage Therapists into one membership with a tailored plan to guide you through the fundamentals of Movement, Mobility and Recovery.
The concept is loosely based on the professional sports model, where every member of our team works together to produce lasting results for you. The final design should illustrate the bespoke nature of our program in a fun, supportive and professional space.
"Whether your aim is to be the best in the world, or the best in your world – it’s all the same to us."
Brand Guidelines
The poster should be on a black background and use our brand colour, lime green (hexcode #cefa08) as a highlight. Please don't overuse the highlight colour though. Generally, we opt for less bright colours and more of a 'street' look
Target Market(s)
The poster should attract predominantly female members, but should not exclude males. The target age range is 30-40 years female.
Industry/Entity Type
Health And Wellness
Font styles to use
Requirements
Must have
- Must Include
• VFS logo
• Tag line " Building Strong, Mobile, Bulletproof Humans"
• Call to action "Join us"
• Sized to 600(W)x900(H)mm
• Text: "A first of it's kind membership, The Veltracore Fitness Studio combines the skills of our industry-leading Physiotherapists, Strength Coaches and Massage Therapists into one membership with a tailored plan to guide you through the fundamentals of Movement, Mobility and Recovery."
Nice to have
- Ideal Inclusions
• Veltracore logo
• Text "Membership Now Open"
• Web address: veltracore.com.au
Should not have
- Don't Use:
• Too much of the highlight colour
• Cartoon imagery
• Images that are too staged or revealing (clothing). Image should fit our target market of everyday active people, not elite athletes or models.

```html
<!DOCTYPE html>
<html lang="en">
<head>
<meta charset="utf-8">
<title>Veltracore Fitness Studio – Membership Poster</title>
<link href="https://fonts.googleapis.com/css2?family=Bebas+Neue&family=Lato:wght@400;700;900&display=swap" rel="stylesheet">
<style>
  :root {
    --stage: #e6e6e6;
    --poster-bg: #1c1c1c;
    --poster-bg-dark: #101010;
    --lime: #cefa08;
    --white: #ffffff;
    --ink: #111111;
    --ghost: #2c2c2c;
    --ghost-bar: #303030;
    --photo-dark: #2e2b33;
    --photo-light: #8f8b96;
  }
  * { margin: 0; padding: 0; box-sizing: border-box; }
  html, body { width: 994px; height: 1200px; overflow: hidden; background: var(--stage); }
  .canvas { position: relative; width: 994px; height: 1200px; overflow: hidden; }
  .poster {
    position: absolute; left: 96px; top: 0;
    width: 968px; height: 1449px;
    transform: scale(0.8282); transform-origin: 0 0;
    background: linear-gradient(180deg, #222 0%, var(--poster-bg) 55%, var(--poster-bg-dark) 75%, var(--poster-bg-dark) 100%);
    overflow: hidden;
    font-family: "Lato", sans-serif;
  }
  .club-name {
    position: absolute; left: 0; top: 50px; width: 968px; text-align: center;
    font: 900 54px/1 "Lato", sans-serif; color: var(--ghost); letter-spacing: -1px;
  }
  .club-bar { position: absolute; left: 88px; top: 140px; width: 790px; height: 30px; background: var(--ghost-bar); }
  .club-initials {
    position: absolute; left: 80px; top: 215px; width: 810px;
    font: 900 430px/1 "Lato", sans-serif; color: #252525; letter-spacing: -10px;
  }
  .hero-photo {
    position: absolute; left: 60px; top: 215px; width: 875px; height: 575px;
    background: linear-gradient(120deg, var(--photo-dark) 0%, #3a3640 45%, var(--photo-light) 100%);
    opacity: 0.75;
  }
  .shapes { position: absolute; left: 0; top: 0; }
  .tagline {
    position: absolute; left: 32px; top: 866px; width: 903px; text-align: center;
    font: 400 90px/72px "Bebas Neue", sans-serif; color: var(--ink);
  }
  .intro {
    position: absolute; left: 385px; top: 1078px; width: 570px;
    border-left: 3px solid var(--lime); padding-left: 20px;
    font: 400 18.5px/24.6px "Lato", sans-serif; color: var(--white);
  }
  .brand-name {
    position: absolute; left: 430px; top: 1262px; width: 360px; text-align: center;
    font: 700 60px/1 "Lato", sans-serif; color: var(--white); letter-spacing: -1px;
  }
  .cta {
    position: absolute; left: 52px; top: 1360px;
    font: 900 58px/1 "Lato", sans-serif; color: var(--lime);
  }
  .web-address {
    position: absolute; left: 345px; top: 1370px; width: 545px; text-align: center;
    font: 700 43px/1 "Lato", sans-serif; color: var(--ink);
  }
  .ribbon-label { font-family: "Lato", sans-serif; font-weight: 900; fill: var(--ink); }
</style>
</head>
<body>
<div class="canvas">
  <div class="poster">
    <div class="club-name">VELTRACORE FITNESS STUDIO</div>
    <div class="club-bar"></div>
    <div class="club-initials">VFS</div>

    <div class="hero-photo" role="img" aria-label="Photo of a smiling woman in black activewear doing a crunch on a silver exercise ball"></div>

    <svg class="shapes" width="968" height="1449" viewBox="0 0 968 1449">
      <polygon points="32,618 483,750 935,618 935,660 483,793 32,660" fill="var(--white)"/>
      <polygon points="32,700 483,835 935,700 935,1025 32,1025" fill="var(--lime)"/>
      <polygon points="318,1352 928,1352 928,1430 290,1430" fill="var(--white)"/>
    </svg>

    <div class="tagline">Building strong,<br>mobile, bulletproof humans</div>

    <svg class="shapes" width="968" height="1449" viewBox="0 0 968 1449">
      <g class="membership-ribbon">
        <g stroke="var(--white)" stroke-width="6" stroke-linecap="round">
          <line x1="45" y1="1078" x2="65" y2="1090"/>
          <line x1="60" y1="1062" x2="73" y2="1084"/>
          <line x1="84" y1="1068" x2="84" y2="1088"/>
          <line x1="340" y1="1240" x2="355" y2="1262"/>
          <line x1="356" y1="1232" x2="368" y2="1250"/>
          <line x1="372" y1="1228" x2="356" y2="1236"/>
        </g>
        <polygon points="50,1095 330,1055 355,1130 65,1165" fill="var(--lime)"/>
        <polygon points="50,1255 345,1210 330,1252 65,1292" fill="var(--lime)"/>
        <polygon points="33,1180 355,1130 345,1210 50,1255" fill="var(--white)"/>
        <text class="ribbon-label" font-size="34" textLength="235" lengthAdjust="spacingAndGlyphs" transform="translate(75 1152) rotate(-8)">MEMBERSHIP</text>
        <text class="ribbon-label" font-size="48" textLength="272" lengthAdjust="spacingAndGlyphs" transform="translate(56 1240) rotate(-8)">NOW OPEN</text>
        <polygon points="150,1308 318,1268 300,1290 155,1320" fill="var(--white)"/>
        <polygon points="205,1318 228,1310 205,1342" fill="var(--white)"/>
      </g>
    </svg>

    <p class="intro">A first of it's kind membership, The Veltracore Fitness Studio combines the skills of our industry-leading Physiotherapists, Strength Coaches and Massage Therapists into one membership with a tailored plan to guide you through the fundamentals of Movement, Mobility and Recovery.</p>

    <div class="brand-name">veltracore</div>
    <div class="cta">JOIN US</div>
    <div class="web-address">www.veltracore.com.au</div>
  </div>
</div>
</body>
</html>
```